Property Management business needs Business cards designed

We provide a premium property management service based in Sydney's Norther Beaches. We want people to feel confident in choosing us to manage their investment properties. We offer a much more personalized service than other estate agents.
We want a modern clean design. Something that shows confidence without being complicated.
Logo attached.

Target Market(s)

35-70yo Male and Female with strong property portfolios within Sydney's Norther Beaches

Industry/Entity Type

Property Management

Contact Information for Business Card

Address: Suite 7, 12-14 Kelvin Parade, Harlow NSW 2188
Two separate named cards.
Tom Ardley - 0491 570 118 tom@harbourvaleestates.com.au
Clara Dunmore - 0491 570 263 clara@harbourvaleestates.com.au

Requirements
Must have
• Business logo, name, number, address, email.

```html
<!DOCTYPE html>
<html lang="en">
<head>
<meta charset="utf-8">
<title>Harbourvale Estates – Business Cards</title>
<link href="https://fonts.googleapis.com/css2?family=Source+Sans+3:wght@400;600;700&display=swap" rel="stylesheet">
<style>
  :root{
    --backdrop:#e6e9eb;
    --card:#fbfcfc;
    --card-edge:#d4dadd;
    --ink:#141414;
    --teal-name:#1d5566;
    --teal-light:#2a7b80;
    --teal-dark:#0f4b5b;
    --rule:#222;
  }
  *{margin:0;padding:0;box-sizing:border-box}
  html,body{width:1200px;height:1000px;overflow:hidden}
  body{background:var(--backdrop);position:relative;font-family:"Source Sans 3",Arial,sans-serif;color:var(--ink)}
  .business-card{position:absolute;left:265px;width:665px;height:397px;background:var(--card);border:1px solid var(--card-edge);overflow:hidden}
  .business-card--tom{top:73px}
  .business-card--clara{top:533px}
  .brand{position:absolute;right:31px;top:88px;display:flex;align-items:center;gap:10px}
  .brand__square{width:18px;height:18px;background:var(--teal-dark)}
  .brand__name{font-weight:700;font-size:34px;letter-spacing:-0.5px;color:var(--ink);line-height:1}
  .person-name{position:absolute;left:33px;top:213px;font-weight:600;font-size:27px;color:var(--teal-name);line-height:1}
  .divider{position:absolute;left:33px;right:31px;top:256px;height:2px;background:var(--rule)}
  .contact-list{position:absolute;left:33px;top:287px;list-style:none}
  .contact-list li{display:flex;align-items:center;gap:9px;font-size:17px;height:30px}
  .contact-list svg{flex:none}
  .address{position:absolute;right:31px;top:287px;text-align:right;font-size:17px;line-height:25px;font-style:normal}
  .accent-band{position:absolute;left:0;bottom:0}
</style>
</head>
<body>

<section class="business-card business-card--tom">
  <div class="brand"><span class="brand__square"></span><span class="brand__name">HARBOURVALE ESTATES</span></div>
  <h2 class="person-name">Tom Ardley</h2>
  <div class="divider"></div>
  <ul class="contact-list">
    <li><svg width="11" height="16" viewBox="0 0 11 16"><rect x="1" y="1" width="9" height="14" rx="2" fill="none" stroke="#333" stroke-width="1.6"/><rect x="4" y="12" width="3" height="1.4" fill="#333"/></svg>0491 570 118</li>
    <li><svg width="15" height="11" viewBox="0 0 15 11"><rect width="15" height="11" fill="#333"/><path d="M0 0 L7.5 6 L15 0" fill="none" stroke="#fff" stroke-width="1.2"/></svg>tom@harbourvaleestates.com.au</li>
  </ul>
  <address class="address">Suite 7, 12-14 Kelvin Parade,<br>Harlow NSW 2188</address>
  <svg class="accent-band" width="665" height="33" viewBox="0 0 665 33">
    <rect x="0" y="15" width="665" height="18" fill="var(--teal-light)"/>
    <polygon points="313,33 340,0 665,0 665,33" fill="var(--teal-dark)"/>
  </svg>
</section>

<section class="business-card business-card--clara">
  <div class="brand"><span class="brand__square"></span><span class="brand__name">HARBOURVALE ESTATES</span></div>
  <h2 class="person-name">Clara Dunmore</h2>
  <div class="divider"></div>
  <ul class="contact-list">
    <li><svg width="11" height="16" viewBox="0 0 11 16"><rect x="1" y="1" width="9" height="14" rx="2" fill="none" stroke="#333" stroke-width="1.6"/><rect x="4" y="12" width="3" height="1.4" fill="#333"/></svg>0491 570 263</li>
    <li><svg width="15" height="11" viewBox="0 0 15 11"><rect width="15" height="11" fill="#333"/><path d="M0 0 L7.5 6 L15 0" fill="none" stroke="#fff" stroke-width="1.2"/></svg>clara@harbourvaleestates.com.au</li>
  </ul>
  <address class="address">Suite 7, 12-14 Kelvin Parade,<br>Harlow NSW 2188</address>
  <svg class="accent-band" width="665" height="33" viewBox="0 0 665 33">
    <rect x="0" y="15" width="665" height="18" fill="var(--teal-light)"/>
    <polygon points="348,33 375,0 665,0 665,33" fill="var(--teal-dark)"/>
  </svg>
</section>

</body>
</html>
```